Website Design for StackHaven As a Service

We are building a service to allow customers to own their own private clouds easily and cheaply. Owning your own private cloud saves costs, and offers more flexibility than a public cloud provider but has historically been a complex and expensive option.

We plan to offer a service where we build and maintain your own private cloud on your own hardware for a cheap monthly costs. Similar to this service - https://nimbarvo.com/solutions/private-cloud

We already have a logo and branding in place - we'd like a website design to be tailored from this branding, see attached logo design.

Feel free to add important elements on the home page such as testimonials, client/partner logos, contact form, social media, etc using placeholder contents in addition to the document we attached.

We also plan to add sub-pages in the future so please make sure that your website design has a full navigation menu.

An example of the site we like: https://www.vosketri.com/ we'd be happy for you to take inspiration from this website.

Target Market(s)

B2B focused, we are targeting start-up/small/medium sized companies who needs help with their cloud and IT infrastructure.

Industry/Entity Type

IT

Number of Pages Required

1 page

Font styles to use
Other font styles liked:
• Please refer to the attachment - font must have Mayeka Demi Bold & Retroica

Requirements
Must have
• Please add placeholder menu since we're planning to have subpages later on.

```html
<!DOCTYPE html>
<html lang="en">
<head>
<meta charset="utf-8">
<title>StackHaven – Private Cloud as a Service</title>
<link rel="stylesheet" href="https://fonts.googleapis.com/css2?family=Lexend:wght@400;500;600;700&family=Didact+Gothic&display=swap">
<style>
:root{
  --blue:#1a82d6;
  --blue-dark:#0b72c4;
  --blue-light:#e8f3fc;
  --ink:#1b1f24;
  --text:#4a525b;
  --white:#ffffff;
  --footer:#1f2429;
  --footer-text:#d7dbe0;
  --head:"Lexend",sans-serif;
  --body:"Didact Gothic",sans-serif;
}
*{margin:0;padding:0;box-sizing:border-box}
html,body{width:1200px;height:3833px;overflow:hidden}
body{position:relative;background:var(--white);font-family:var(--body);color:var(--text)}
.abs{position:absolute}
.btn{position:absolute;display:flex;align-items:center;justify-content:center;border-radius:9px;font-family:var(--head);font-weight:600;font-size:16px;text-decoration:none}
.btn-solid{background:linear-gradient(90deg,#2e95e3,#1478cc);color:var(--white);box-shadow:0 8px 18px rgba(26,130,214,.3)}
.btn-white{background:var(--white);color:var(--blue);border:3px solid #9fd0f5}
h1,h2,h3{font-family:var(--head);color:var(--ink)}

/* header */
.brand{position:absolute;display:flex;align-items:center;gap:8px;font-family:var(--head);font-weight:600;font-size:22px;color:var(--blue)}
.brand-dot{width:26px;height:26px;border-radius:50%;background:var(--blue)}
.nav{position:absolute;top:36px;font-family:var(--head);font-size:14px;color:var(--ink)}
.nav a{position:absolute;white-space:nowrap;color:inherit;text-decoration:none}
.login{left:925px;top:28px;width:98px;height:36px;border:2px solid var(--blue);color:var(--blue);font-size:14px;border-radius:10px}
.signup{left:1039px;top:28px;width:113px;height:36px;font-size:14px;border-radius:10px}

/* hero */
.hero-title{left:75px;top:174px;font-size:30px;line-height:39px;font-weight:600}
.hero-copy{left:75px;top:305px;width:500px;font-size:15px;line-height:22.5px}
.hero-note{left:75px;top:397px;width:500px;font-family:var(--head);font-weight:600;font-size:15px;line-height:22.5px;color:var(--blue)}
.hero-cta{left:75px;top:466px;width:175px;height:54px;gap:8px}
.hero-swoosh{left:560px;top:120px;width:640px;height:560px}
.hero-art{left:737px;top:164px;width:380px;height:357px;border-radius:24px;background:linear-gradient(150deg,#cfe7fb,#3f9de6 60%,#1f2b3a)}

/* benefits */
.benefits{left:0;top:676px;width:1200px;height:850px;background:linear-gradient(135deg,#2a92e2,#0a74c6)}
.section-title{position:absolute;left:0;width:1200px;text-align:center;font-size:30px;line-height:39px;font-weight:600}
.benefits .section-title{top:58px;color:var(--white)}
.bcard{position:absolute;width:324px;border-radius:10px;background:rgba(255,255,255,.09);border:3px solid rgba(255,255,255,.14);padding:24px 34px;color:var(--white)}
.bcard svg{display:block;width:44px;height:44px;margin-bottom:18px}
.bcard h3{color:var(--white);font-size:16px;line-height:22px;font-weight:600;margin-bottom:12px}
.bcard p{font-size:15px;line-height:22.5px;color:#e5f2fd}
.get-started{left:524px;top:718px;width:168px;height:59px}

/* public cloud cards */
.pcard{position:absolute;top:1739px;width:324px;height:356px;border-radius:10px;background:var(--white);box-shadow:0 6px 30px rgba(20,60,110,.1);padding:33px 36px}
.icon-circle{width:75px;height:75px;border-radius:50%;background:var(--blue-light);display:flex;align-items:center;justify-content:center;margin:0 auto 40px}
.pcard h3{font-size:16px;line-height:22px;font-weight:600;margin-bottom:14px}
.pcard p{font-size:15px;line-height:22.5px}
.lets-talk{left:518px;top:2156px;width:162px;height:52px}

/* feature lists */
.flist{position:absolute;list-style:none}
.flist li{position:relative;padding-left:48px;font-size:15px;line-height:22.5px;margin-bottom:23px}
.flist li::before{content:"";position:absolute;left:0;top:2px;width:22px;height:22px;border-radius:50%;background:var(--blue-light)}
.flist li::after{content:"";position:absolute;left:8px;top:10px;width:6px;height:6px;border-radius:50%;background:var(--blue)}
.art{position:absolute;border-radius:50%}

/* contact band */
.contact{left:0;top:3325px;width:1200px;height:244px;background:linear-gradient(135deg,#2a92e2,#0a74c6)}
.contact .section-title{top:58px;color:var(--white)}
.detail{left:517px;top:126px;width:165px;height:59px}

/* footer */
.footer{left:0;top:3569px;width:1200px;height:264px;background:var(--footer);color:var(--footer-text);font-size:14px}
.finfo{position:absolute;left:78px;display:flex;align-items:center;gap:14px;font-family:var(--head)}
.finfo svg{width:14px;height:14px}
.fbrand{left:502px;top:46px;color:var(--white);font-size:22px}
.fbrand .brand-dot{background:var(--white);width:22px;height:22px}
.fnav a{position:absolute;top:116px;color:var(--footer-text);font-family:var(--head);text-decoration:none}
.follow{left:491px;top:152px;display:flex;align-items:center;gap:12px;font-family:var(--head)}
.social{width:20px;height:20px;border-radius:4px;border:2px solid var(--footer-text)}
.store{position:absolute;left:963px;width:161px;height:52px;border:1px solid #8b939c;border-radius:8px;display:flex;align-items:center;gap:14px;padding-left:26px;font-family:var(--head);color:var(--white)}
.store span.mark{width:18px;height:18px;border-radius:50%;background:var(--white)}
.fline{left:0;top:212px;width:1200px;height:1px;background:#3a4148}
.copy{left:0;top:230px;width:1200px;text-align:center;font-size:12px;font-family:var(--head)}
</style>
</head>
<body>

<header>
  <div class="brand" style="left:45px;top:31px"><span class="brand-dot"></span>StackHaven</div>
  <nav class="nav">
    <a style="left:354px">Products</a><a style="left:460px">Solutions</a><a style="left:562px">Pricing</a><a style="left:652px">Resources</a><a style="left:766px">About</a>
  </nav>
  <a class="btn login">Login</a>
  <a class="btn btn-solid signup">Sign Up</a>
</header>

<section class="hero">
  <svg class="abs hero-swoosh" viewBox="0 0 640 560" aria-hidden="true">
    <path d="M0 480 C200 380 420 300 640 120 L640 560 L0 560 Z" fill="#f1f7fd"/>
    <path d="M60 520 C260 420 460 320 640 200" stroke="#e1eefa" stroke-width="30" fill="none"/>
  </svg>
  <div class="abs hero-art" role="img" aria-label="Illustration of a person uploading to a cloud on a large laptop screen"></div>
  <h1 class="abs hero-title">A Groundbreaking Way For<br>Your Small Business To Benefit<br>From The Power Of The Cloud</h1>
  <p class="abs hero-copy">StackHaven as a Service is here to help small businesses utilise the power of the cloud without complicated set-ups or scary price tags</p>
  <p class="abs hero-note">Ready to modernise your infrastructure with a fully managed private cloud solution from SHaaS?</p>
  <a class="btn btn-solid hero-cta"><svg width="14" height="14" viewBox="0 0 24 24"><path fill="#fff" d="M6.6 10.8a15 15 0 006.6 6.6l2.2-2.2a1 1 0 011-.25 11 11 0 003.6.6 1 1 0 011 1V20a1 1 0 01-1 1A17 17 0 013 4a1 1 0 011-1h3.5a1 1 0 011 1 11 11 0 00.6 3.6 1 1 0 01-.25 1z"/></svg>Contact Us</a>
</section>

<section class="abs benefits">
  <h2 class="section-title">How SHAAS Benefits<br>Your Business</h2>
  <div class="bcard" style="left:75px;top:194px;height:210px">
    <svg viewBox="0 0 44 44" fill="none" stroke="#fff" stroke-width="3" stroke-linecap="round"><path d="M4 12h24a5 5 0 10-5-5M4 22h34a5 5 0 11-5 5M8 32h18"/></svg>
    <h3>Totally Flexible</h3><p>Get the cloud you want and the latest innovations you need</p>
  </div>
  <div class="bcard" style="left:438px;top:194px;height:210px">
    <svg viewBox="0 0 44 44"><path fill="#fff" d="M2 8l20 14L2 36zM22 8l20 14-20 14z"/></svg>
    <h3>Faster</h3><p>Our private cloud solutions outpace public clouds</p>
  </div>
  <div class="bcard" style="left:800px;top:194px;height:210px">
    <svg viewBox="0 0 44 44" fill="none" stroke="#fff" stroke-width="3"><rect x="3" y="10" width="36" height="24" rx="3"/><circle cx="21" cy="22" r="5"/><path d="M4 4l36 36"/></svg>
    <h3>No Consultancy Fees</h3><p>We'll work with you and charge set fees for everything</p>
  </div>
  <div class="bcard" style="left:75px;top:429px;height:232px">
    <svg viewBox="0 0 44 44" fill="none" stroke="#fff" stroke-width="3"><rect x="3" y="8" width="38" height="26" rx="4"/><circle cx="22" cy="21" r="6"/></svg>
    <h3>Greater Value<br>For Money</h3><p>Totally transparent pricing for no nasty month-end surprises</p>
  </div>
  <div class="bcard" style="left:438px;top:429px;height:232px">
    <svg viewBox="0 0 44 44" fill="none" stroke="#fff" stroke-width="3.5" stroke-linecap="round"><path d="M6 38L30 14M30 14a8 8 0 109-9l-5 5-4-1-1-4 5-5M8 6l28 32M6 10l4-4"/></svg>
    <h3>Management, Monitoring<br>And Maintenance</h3><p>They're all included in your monthly price</p>
  </div>
  <div class="bcard" style="left:800px;top:429px;height:232px">
    <svg viewBox="0 0 44 44"><path fill="#fff" d="M22 2l17 6v12c0 11-8 19-17 22C13 39 5 31 5 20V8z"/><path d="M14 22l6 6 11-11" stroke="#1a82d6" stroke-width="4" fill="none"/></svg>
    <h3>Tried And Tested Cloud<br>Solutions</h3><p>We'll deploy the right OpenVale solutions for your business</p>
  </div>
  <a class="btn btn-white get-started">Get Started</a>
</section>

<section class="public">
  <h2 class="section-title" style="top:1593px">If You're Using A<br>Public Cloud Now...</h2>
  <div class="pcard" style="left:75px">
    <div class="icon-circle"><svg width="38" height="38" viewBox="0 0 38 38"><path fill="#1a82d6" d="M13 4h12l-3 6h-6zM19 11c9 0 15 7 15 15 0 6-5 9-15 9S4 32 4 26c0-8 6-15 15-15z"/><text x="19" y="31" text-anchor="middle" fill="#fff" font-family="Lexend,sans-serif" font-size="15" font-weight="700">$</text></svg></div>
    <h3>You Could Be Paying<br>Too Much</h3>
    <p>Public cloud pricing structures have a habit of sneakily scaling up very quickly. With SHAAS, you'll always know what you're paying for your private cloud services.</p>
  </div>
  <div class="pcard" style="left:438px">
    <div class="icon-circle"><svg width="36" height="36" viewBox="0 0 36 36" fill="none" stroke="#1a82d6" stroke-width="3"><rect x="4" y="4" width="28" height="8"/><rect x="4" y="14" width="28" height="8"/><rect x="4" y="24" width="28" height="8"/><path d="M2 2l32 32"/></svg></div>
    <h3>You're Likely Not Getting The Benefits Of Full Functionality</h3>
    <p>Public cloud providers cannot adopt new innovations and functions as quickly and easily as the private cloud solutions you'll get from SHAAS.</p>
  </div>
  <div class="pcard" style="left:800px">
    <div class="icon-circle"><svg width="38" height="38" viewBox="0 0 38 38" fill="#1a82d6"><circle cx="14" cy="14" r="9"/><circle cx="14" cy="14" r="3.5" fill="#e8f3fc"/><circle cx="28" cy="28" r="6"/><circle cx="28" cy="28" r="2.2" fill="#e8f3fc"/></svg></div>
    <h3>You'll Be Tied To The Services Your Provider Can Provide</h3>
    <p>Public cloud providers will have a limited suite of products and services to offer you. A SHAAS private cloud has no such limitations.</p>
  </div>
  <a class="btn btn-solid lets-talk">Let's Talk</a>
</section>

<section class="features">
  <h2 class="section-title" style="top:2352px">If You're Using A<br>Public Cloud Now...</h2>
  <div class="art" role="img" aria-label="Illustration of a person giving a thumbs up beside a checklist card" style="left:149px;top:2531px;width:330px;height:283px;border-radius:50% 50% 40px 40px;background:linear-gradient(160deg,#ffffff,#d8ebfb)"></div>
  <ul class="flist" style="left:582px;top:2505px;width:460px">
    <li>We'll quickly get to grips with what your organisation needs, and deliver it via our private cloud solutions.</li>
    <li>Enjoy the ease of the public cloud, combined with the features, innovations and flexibility of the private cloud.</li>
    <li>You can focus on your core business while we support you with a dedicated cloud infrastructure.</li>
    <li>We'll create and deliver the launchpad that will take your business forward.</li>
  </ul>
  <ul class="flist" style="left:129px;top:2950px;width:470px">
    <li>Get the benefits of your own cloud infrastructure and reduce your operational costs.</li>
    <li>Fast and easy computing, storage and network resources.</li>
    <li>Managed operations from private OpenVale clouds and Kubrane.</li>
    <li>We'll support your growth and scale your cloud as you need it.</li>
  </ul>
  <div class="art" role="img" aria-label="Illustration of a person presenting rising bar and line charts" style="left:707px;top:2918px;width:305px;height:335px;border-radius:50% 50% 30px 30px;background:linear-gradient(160deg,#ffffff,#d8ebfb)"></div>
</section>

<section class="abs contact">
  <h2 class="section-title">Contact Us</h2>
  <a class="btn btn-white detail">Detail Here</a>
</section>

<footer class="abs footer">
  <div class="finfo" style="top:66px"><svg viewBox="0 0 24 24"><path fill="#fff" d="M12 2a7 7 0 00-7 7c0 5 7 13 7 13s7-8 7-13a7 7 0 00-7-7zm0 10a3 3 0 110-6 3 3 0 010 6z"/></svg>Larkfield, Oregon, US</div>
  <div class="finfo" style="top:96px"><svg viewBox="0 0 24 24"><path fill="#fff" d="M6.6 10.8a15 15 0 006.6 6.6l2.2-2.2a1 1 0 011-.25 11 11 0 003.6.6 1 1 0 011 1V20a1 1 0 01-1 1A17 17 0 013 4a1 1 0 011-1h3.5a1 1 0 011 1 11 11 0 00.6 3.6 1 1 0 01-.25 1z"/></svg>555 018 234</div>
  <div class="finfo" style="top:127px"><svg viewBox="0 0 24 24"><path fill="#fff" d="M2 5h20v14H2zm2 2v.5l8 5 8-5V7l-8 5z"/></svg>hello@stackhaven.io</div>
  <div class="brand fbrand"><span class="brand-dot"></span>StackHaven</div>
  <nav class="fnav">
    <a style="left:380px">Products</a><a style="left:480px">Solutions</a><a style="left:582px">Pricing</a><a style="left:667px">Resources</a><a style="left:778px">About</a>
  </nav>
  <div class="abs follow">Follow Us : <span class="social"></span><span class="social"></span><span class="social"></span><span class="social"></span></div>
  <div class="store" style="top:45px"><span class="mark"></span>App Market</div>
  <div class="store" style="top:112px"><span class="mark"></span>Play Bazaar</div>
  <div class="abs fline"></div>
  <p class="abs copy">© 2022 StackHaven All Rights Reserved.</p>
</footer>

</body>
</html>
```